resdesign signage banners for mortgage broking firm rates

Kestrel Rise logo at the top
Bank logos down the bottom
Rates box white, with blue writing
"Variable Rate Today!"
(space for rates, change all the time)
Variable Rate Comparison Rate

Fixed Rate Today!

Fixed rate Comparsion rate

The backgroud should be blue and fade down to white with the logos at the bottom

Below the rates boxes

should have

"Kestrel Rise returns 0.15% to you every year! That is $750 on $500,000 loan."

attached is pictures of the previous banners

1.4m L
80 cm W
for the pull up banner

We want the banner similar, just a new updated design.
Updates

Project Deadline Extended Reason: The managing director came back and thought the design looked to busy, he wants a simpler design similar to previous. Added Wednesday, April 20, 2016

Industry/Entity Type

Finance

Colors
fbee3d
fbed22
33a6d7
0292cd
ffffff

Requirements
Must have
• Bank logos down the bottom
• Rates section for variable and fixed
• Kestrel Rise Home Loan logo
• Blue writing
• white back ground for rates box.
• Fade from sky blue at the top down to white where to logos are
• The cloud behind the logo like the attached picture.
Nice to have
• New modern design

```html
<!DOCTYPE html>
<html lang="en">
<head>
<meta charset="utf-8">
<title>Kestrel Rise Home Loans – Rates Banner</title>
<link href="https://fonts.googleapis.com/css2?family=PT+Sans+Narrow:wght@700&family=Ubuntu:wght@400;500&display=swap" rel="stylesheet">
<style>
  :root {
    --sky: #8fd0f0;
    --sky-deep: #33a6d7;
    --brand-blue: #1f6fb8;
    --ink-blue: #1d4f8c;
    --gold: #f4b81d;
    --white: #ffffff;
    --page: #f3f4f6;
    --lender-red: #d22a2a;
  }
  * { margin: 0; padding: 0; box-sizing: border-box; }
  html, body { width: 1200px; height: 1010px; overflow: hidden; background: var(--page); }
  .banner {
    position: absolute; left: 330px; top: 25px; width: 540px; height: 960px;
    background: linear-gradient(to bottom, var(--sky) 0%, var(--sky) 64%, var(--white) 82%, var(--white) 100%);
    font-family: "Ubuntu", sans-serif;
    box-shadow: 0 2px 10px rgba(0,0,0,0.12);
  }
  .brand {
    position: absolute; top: 34px; left: 0; width: 100%;
    display: flex; justify-content: center; align-items: center; gap: 14px;
  }
  .brand-mark { width: 58px; height: 58px; border-radius: 50%; background: var(--sky-deep); }
  .brand-name {
    font-family: "Ubuntu", sans-serif; font-weight: 500; color: var(--ink-blue);
    font-size: 40px; line-height: 1; letter-spacing: 1px;
  }
  .brand-name span { display: block; font-size: 17px; letter-spacing: 9px; margin-top: 6px; }
  .rate-panel {
    position: absolute; left: 28px; width: 484px; height: 240px;
    background: var(--gold); border-radius: 4px;
  }
  .rate-panel.variable { top: 172px; }
  .rate-panel.fixed { top: 424px; }
  .rate-title, .rate-labels {
    font-family: "PT Sans Narrow", sans-serif; font-weight: 700; color: var(--white);
    text-transform: uppercase; text-align: center;
  }
  .rate-title { height: 46px; line-height: 50px; font-size: 25px; }
  .rate-figures {
    margin: 0 5px; height: 146px; background: var(--white);
    display: flex; align-items: center;
  }
  .rate-figures div, .rate-labels div { flex: 1; text-align: center; }
  .rate-figures div { font-family: "Ubuntu", sans-serif; font-weight: 500; font-size: 66px; color: var(--brand-blue); }
  .rate-labels { display: flex; height: 48px; line-height: 48px; font-size: 21px; }
  .giveback {
    position: absolute; top: 688px; left: 0; width: 100%; text-align: center;
    color: var(--ink-blue); font-size: 25px; line-height: 36px;
  }
  .lenders {
    position: absolute; top: 790px; left: 22px; width: 496px;
    display: flex; flex-wrap: wrap; justify-content: center; gap: 9px 10px;
  }
  .lender {
    display: flex; align-items: center; gap: 4px; width: 72px; height: 20px;
    font-family: "Ubuntu", sans-serif; font-weight: 500; font-size: 9.5px; color: var(--ink-blue);
    white-space: nowrap; overflow: hidden;
  }
  .lender.red { color: var(--lender-red); }
  .lender i { display: inline-block; width: 9px; height: 9px; flex: none; background: currentColor; }
</style>
</head>
<body>
  <div class="banner">
    <header class="brand">
      <div class="brand-mark"></div>
      <div class="brand-name">KESTREL RISE<span>HOME LOANS</span></div>
    </header>

    <section class="rate-panel variable">
      <h2 class="rate-title">Variable Rate Today!</h2>
      <div class="rate-figures"><div>3.98%</div><div>3.99%</div></div>
      <div class="rate-labels"><div>Variable Rate</div><div>Comparison Rate</div></div>
    </section>

    <section class="rate-panel fixed">
      <h2 class="rate-title">Fixed Rate Today!</h2>
      <div class="rate-figures"><div>3.94%</div><div>4.44%</div></div>
      <div class="rate-labels"><div>Fixed Rate</div><div>Comparison Rate</div></div>
    </section>

    <p class="giveback">Kestrel Rise returns 0.15% to you every year!<br>That is $750 on $500,000 loan.</p>

    <div class="lenders">
      <div class="lender"><i></i>Harbourline</div>
      <div class="lender">Tallow Group</div>
      <div class="lender">Amberly</div>
      <div class="lender">Northwyn</div>
      <div class="lender red"><i></i>Eastmere</div>
      <div class="lender">Coralbay Bank</div>
      <div class="lender red">Ridgeport</div>
      <div class="lender red"><i></i>Westholm</div>
      <div class="lender">Slatestone</div>
      <div class="lender">Quayside</div>
      <div class="lender"><i></i>Anchor Fin.</div>
      <div class="lender">Meridian</div>
      <div class="lender"><i></i>Brightfield</div>
      <div class="lender"><i></i>Keyfund</div>
      <div class="lender">Pliant</div>
      <div class="lender"><i></i>Orbis Money</div>
      <div class="lender red">Heathcote</div>
      <div class="lender">Dwellstart</div>
      <div class="lender red">Lantern Dir.</div>
      <div class="lender red"><i></i>Doorway</div>
      <div class="lender"><i></i>Larkhill</div>
      <div class="lender">Freehold</div>
      <div class="lender"><i></i>Marrowick</div>
      <div class="lender"><i></i>Ours Bank</div>
      <div class="lender">Fenwick Cap.</div>
      <div class="lender red"><i></i>Pinnacle Co</div>
      <div class="lender">Nowra Fin.</div>
      <div class="lender red">Tidal Bank</div>
      <div class="lender">Saltmark</div>
      <div class="lender">Mindset</div>
      <div class="lender"><i></i>Baywide</div>
      <div class="lender"><i></i>Granite</div>
      <div class="lender">Southcrest</div>
    </div>
  </div>
</body>
</html>
```